Fahnendesign für Lenz & Baumer Elektrotechnik
Zielgruppe
Lenz & Baumer Elektrotechnik hat sich spezialisiert auf die Errichtung elektrischer Anlagen im Wohn-Neubau und bei Sanierungen von Wohnungen und Einfamilienhäusern. Unsere Zielgruppe sind Bauunternehmen und private Bauherren.
Aufgabenstellung
-Design nach Vorgaben Druckfalke ( Befestigung links )
Natürlich soll unser Logo gut zu sehen sein sowie unsere Internetseite : www.lenz-baumer.de
Firmenschriftart: Titel Fira Sans , Schrift : Montserrat
Vielleicht kann ein Bezug auf die Positionierung hergestellt werden , ist aber kein muss.
Alles andere kann kreativ entschieden werden. Schaut gerne auf unsere Social Media Kanäle:
https://www.instagram.com/lenz_baumer_elektrotechnik/?hl=de
https://www.facebook.com/lenzbaumerelektrotechnik/

```html
<!DOCTYPE html>
<html lang="de">
<head>
<meta charset="utf-8">
<title>Lenz &amp; Baumer Elektrotechnik – Fahne</title>
<link rel="stylesheet" href="https://fonts.googleapis.com/css2?family=Montserrat:wght@400;600&display=swap">
<style>
  :root {
    --backdrop: #e0e0e0;
    --banner-white: #f6f6f6;
    --brand-blue: #2a9fd6;
    --panel-blue-top: #1f98cc;
    --panel-blue-bottom: #0d7dbf;
    --sidebar-blue: #1d5a96;
    --text-light: #ffffff;
  }
  html, body {
    margin: 0;
    padding: 0;
    width: 1200px;
    height: 960px;
    overflow: hidden;
    background: var(--backdrop);
  }
  .canvas {
    position: relative;
    width: 1200px;
    height: 960px;
  }
  .flag {
    position: absolute;
    left: 401px;
    top: 40px;
    width: 397px;
    height: 880px;
    box-shadow: 0 6px 18px rgba(0, 0, 0, 0.12);
  }
  .flag svg { display: block; width: 100%; height: 100%; }
  .brand-name {
    font-family: "Montserrat", sans-serif;
    font-weight: 600;
    fill: var(--brand-blue);
  }
  .contact-text {
    font-family: "Montserrat", sans-serif;
    font-weight: 400;
    font-size: 27px;
    fill: var(--text-light);
  }
</style>
</head>
<body>
<main class="canvas">
  <div class="flag">
    <svg viewBox="0 0 636 1410" xmlns="http://www.w3.org/2000/svg" role="img" aria-label="Fahne Lenz &amp; Baumer Elektrotechnik">
      <defs>
        <linearGradient id="panelGradient" x1="0" y1="0" x2="0" y2="1">
          <stop offset="0" stop-color="var(--panel-blue-top)"/>
          <stop offset="1" stop-color="var(--panel-blue-bottom)"/>
        </linearGradient>
        <linearGradient id="whiteGradient" x1="0" y1="0" x2="0" y2="1">
          <stop offset="0" stop-color="#ffffff"/>
          <stop offset="1" stop-color="#ececec"/>
        </linearGradient>
      </defs>

      <!-- white upper field -->
      <rect class="flag-field" x="0" y="0" width="636" height="1410" fill="url(#whiteGradient)"/>

      <!-- brand block -->
      <g class="brand-block">
        <circle cx="318" cy="190" r="72" fill="none" stroke="var(--brand-blue)" stroke-width="6"/>
        <text class="brand-name" x="318" y="338" font-size="50" text-anchor="middle">LENZ &amp; BAUMER</text>
        <text class="brand-name" x="318" y="378" font-size="24" text-anchor="middle" letter-spacing="6">ELEKTROTECHNIK</text>
      </g>

      <!-- diagonal accent stripe -->
      <polygon class="accent-stripe" points="0,660 636,506 636,532 0,688" fill="var(--brand-blue)"/>

      <!-- blue lower panel -->
      <polygon class="contact-panel" points="0,704 636,545 636,1410 0,1410" fill="url(#panelGradient)"/>
      <polygon class="icon-sidebar" points="0,704 133,671 133,1410 0,1410" fill="var(--sidebar-blue)"/>

      <!-- contact rows -->
      <g class="contact-row website">
        <g fill="none" stroke="var(--text-light)" stroke-width="4">
          <circle cx="67" cy="1051" r="23"/>
          <ellipse cx="67" cy="1051" rx="10" ry="23"/>
          <line x1="44" y1="1051" x2="90" y2="1051"/>
        </g>
        <text class="contact-text" x="163" y="1058">www.lenz-baumer.de</text>
      </g>

      <g class="contact-row instagram">
        <rect x="42" y="1142" width="50" height="50" rx="12" fill="none" stroke="var(--text-light)" stroke-width="4"/>
        <text class="contact-text" x="163" y="1176">lenz_baumer_elektrotechnik</text>
      </g>

      <g class="contact-row facebook">
        <circle cx="68" cy="1286" r="28" fill="var(--text-light)"/>
        <text class="contact-text" x="163" y="1293">@lenzbaumerelektrotechnik</text>
      </g>
    </svg>
  </div>
</main>
</body>
</html>
```